Quirky Label Design for an Exciting UK-Based Organic Skincare Company!

We need label designs across our range of products, we are a high quality yet quirky organic skincare company called Gently Lumora, we use frosted glass packaging, and we are just wanting one design done for now, but the winning designer we would want to work with to design the rest of the labels for us. We also want them to design business cards and other literature at some point and maybe even a website page.

Our label design will go on a 63mm tall frosted glass jar which is 62mm in diameter. The actual label dimensions should be, 170 mm (W) x 50 mm (H). The idea is so that it wraps around the whole jar with the design at one side (at the front) and the ingredients on another (at the back).

LABEL 1
Organic Polynesian Whipped Body Butter
Vanilla Bean
120ml

Made with Organic Shea and Cocoa Butters and exotic Monoi de Tahiti

Ingredients (INCI): Organic Raw Shea Butter (Butyrospermum Parkii), Organic Raw Cocoa Butter (Theobroma Cacao), Monoi de Tahiti (Coconut (Cocos nucifera) oil (and) Tiare (Gardenia tahitensis) flower), Organic Sweet Almond Oil (Prunus Amygdalus Dulcis), Organic Madagascan Vanilla Extract (Vanillin)

Handmade by Gently Lumora Ltd
14 Quillfield Lane, Bournemouth BH2 9RT, UK
Batch:

OPTIONAL WRITING (if it fits in):
100% Natural and Organic
Intensely Moisturising

LABEL 2
Mango Smoothie
120ml

Ingredients (INCI): Organic Raw Shea Butter (Butyrospermum Parkii), Organic Raw Cocoa Butter (Theobroma Cacao), Monoi de Tahiti (Coconut (Cocos nucifera) oil (and) Tiare (Gardenia tahitensis) flower), Organic Sweet Almond Oil (Prunus Amygdalus Dulcis), Organic Mango Flavour (Aroma)

Batch:

100% Natural and Organic
Intensely Moisturising

I have attached a picture of the jar we use and the lid we use for these products, as well as our logo. I've also attached a 'Handmade in Dorset' stamp which we'd like to go on there if possible, along with a shelf life symbol.

I am thinking the background colour of the labels will be either white or even brown paper colour. Perhaps it would be interesting to see it in both. UPDATE: We have decided on white background now, not brown.

The final design should denote handmade, organic, high quality, pure, yet quirky and original / unique. I am thinking perhaps a seemingly hand-drawn black leaf outline? Could fit the bill, but as I say, up to you. Something that says handmade yet professional.

I'd like to have the original Photoshop files from the winning designer so we can use them as a template for the rest of our horizontal labels.

Target Market(s)

Everyone that appreciates a good quality skincare product focusing on natural & organic. Price is mid-range to high

Industry/Entity Type

It Company

Requirements
Must have
• Must make the product look high quality & organic yet quirky and accessible. Must have our logo and the shelf life symbol and the writing as above.
Nice to have
• Nice to have the 'handmade' stamp attached, but not absolutely necessary if it doesn't fit within your design.

```html
<!DOCTYPE html>
<html lang="en">
<head>
<meta charset="UTF-8">
<title>Gently Lumora – Whipped Body Butter Labels</title>
<link href="https://fonts.googleapis.com/css2?family=Fira+Sans+Condensed:wght@400;500;700&family=Dancing+Script:wght@700&display=swap" rel="stylesheet">
<style>
  :root {
    --canvas: #c9c9c9;
    --paper: #f7f7f5;
    --ink: #1c1c1c;
    --lime: #c5d52a;
    --lime-text: #8fa51e;
    --mango: #f1ab4a;
    --mango-text: #e09a38;
  }
  * { box-sizing: border-box; margin: 0; padding: 0; }
  html, body { width: 1200px; height: 1121px; overflow: hidden; }
  body {
    background: var(--canvas);
    font-family: "Fira Sans Condensed", sans-serif;
    color: var(--ink);
    position: relative;
  }
  .label {
    position: absolute;
    top: 338px;
    width: 480px;
    height: 445px;
    background: var(--paper);
    overflow: hidden;
    box-shadow: 0 6px 18px rgba(0,0,0,0.12);
  }
  .label--vanilla { left: 80px; --accent: var(--lime); --accent-text: var(--lime-text); }
  .label--mango { left: 640px; --accent: var(--mango); --accent-text: var(--mango-text); }

  .leaf-sprig {
    position: absolute;
    top: 8px;
    width: 96px;
    height: 150px;
    border-radius: 40px 40px 20px 20px;
    background: linear-gradient(160deg, var(--accent), transparent 85%);
    opacity: 0.45;
  }
  .leaf-sprig--left { left: 6px; }
  .leaf-sprig--right { right: 6px; }

  .brand {
    position: absolute;
    top: 50px;
    left: 0;
    right: 0;
    text-align: center;
    font-weight: 700;
    font-size: 44px;
    line-height: 1;
    letter-spacing: 1px;
    text-transform: uppercase;
  }

  .product-title {
    position: absolute;
    top: 180px;
    left: 62px;
    width: 356px;
    height: 100px;
    background: var(--accent);
    border-radius: 10px;
    display: flex;
    flex-direction: column;
    justify-content: center;
    align-items: center;
    font-family: "Dancing Script", cursive;
    font-size: 32px;
    line-height: 1.2;
  }

  .variant, .volume {
    position: absolute;
    top: 312px;
    background: var(--accent);
    font-weight: 500;
    text-align: center;
    line-height: 1.05;
  }
  .variant {
    left: 40px;
    width: 70px;
    height: 56px;
    font-size: 18px;
    display: flex; align-items: center; justify-content: center;
  }
  .volume {
    right: 40px;
    width: 70px;
    height: 56px;
    font-size: 22px;
    display: flex; align-items: center; justify-content: center;
  }
  .claims {
    position: absolute;
    top: 318px;
    left: 120px;
    right: 120px;
    text-align: center;
    color: var(--accent-text);
    font-size: 18px;
    line-height: 1.35;
  }

  .ingredient-band {
    position: absolute;
    top: 388px;
    left: 0;
    right: 0;
    height: 58px;
    background: var(--accent);
    white-space: nowrap;
    overflow: hidden;
    font-weight: 500;
    font-size: 19px;
    letter-spacing: 2.5px;
    line-height: 58px;
    text-transform: uppercase;
    padding-left: 2px;
  }
  .ingredient-band span { margin-left: 18px; }
</style>
</head>
<body>

<section class="label label--vanilla">
  <div class="leaf-sprig leaf-sprig--left" role="img" aria-label="Hand-drawn leaf sprig and rose ornament"></div>
  <div class="leaf-sprig leaf-sprig--right" role="img" aria-label="Hand-drawn leaf sprig and rose ornament"></div>
  <div class="brand">Gently<br>Lumora</div>
  <div class="product-title"><span>Organic Polynesian</span><span>Whipped Body Butter</span></div>
  <div class="variant">Vanilla<br>Bean</div>
  <p class="claims">100% Natural And Organic<br>Intensely Moisturising</p>
  <div class="volume">120ml</div>
  <div class="ingredient-band">noi de Tahiti<span>Made with organic shea and cocoa</span></div>
</section>

<section class="label label--mango">
  <div class="leaf-sprig leaf-sprig--left" role="img" aria-label="Hand-drawn leaf sprig and rose ornament"></div>
  <div class="leaf-sprig leaf-sprig--right" role="img" aria-label="Hand-drawn leaf sprig and rose ornament"></div>
  <div class="brand">Gently<br>Lumora</div>
  <div class="product-title"><span>Organic Polynesian</span><span>Whipped Body Butter</span></div>
  <div class="variant">Mango<br>Smoothie</div>
  <p class="claims">100% Natural And Organic<br>Intensely Moisturising</p>
  <div class="volume">120ml</div>
  <div class="ingredient-band">noi de Tahiti<span>Made with organic shea and cocoa</span></div>
</section>

</body>
</html>
```